Vesit cards for web development company

We need a business card design for our company. The company develops online platforms and conducts marketing consulting. Company logo. The cards must fit in with us (a junior start UP), but they must also be professional enough to impress with investors like banks. We wish you a combination of classic and modern design

Target Market(s)

Business partners and IT and marketing customers

Industry/Entity Type

It Company

Contact Information for Business Card

Folgende Information müssen Drauf.
Name, Position, Telefon Nr., Mobile Nr., E-Mail adresse, Optional sind noch Webadresse und HRB Nummer

Colors

Designer to choose colors to be used in the design.

Requirements
Must have
• The cards have to fit into the logo later and have to be dynamic and serious at the same time

```html
<!DOCTYPE html>
<html lang="en">
<head>
<meta charset="utf-8">
<title>Kestrel Development – Business Card</title>
<link rel="stylesheet" href="https://fonts.googleapis.com/css2?family=Montserrat:wght@500;600;700&display=swap">
<style>
  :root {
    --backdrop: #3a3431;
    --card: #1f2225;
    --card-edge: #2a2d31;
    --brand-blue: #2a84d2;
    --steel: #9a9ca0;
    --ink-light: #f2f3f5;
  }
  * { box-sizing: border-box; margin: 0; padding: 0; }
  html, body { width: 1200px; height: 864px; overflow: hidden; }
  body {
    background: var(--backdrop);
    font-family: "Montserrat", Arial, sans-serif;
    position: relative;
  }
  .card {
    position: absolute;
    width: 520px;
    height: 298px;
    background: var(--card);
    border: 1px solid var(--card-edge);
    border-radius: 4px;
    box-shadow: 0 14px 30px rgba(0,0,0,.35);
  }
  .card--front { left: 70px; top: 140px; display: flex; align-items: center; justify-content: center; }
  .card--back { left: 610px; top: 426px; display: flex; align-items: center; padding: 0 34px; }

  .wordmark { display: flex; align-items: center; gap: 12px; color: var(--brand-blue); font-weight: 700; }
  .wordmark__dot { width: 18px; height: 18px; border-radius: 50%; background: var(--brand-blue); flex: none; }
  .card--front .wordmark { font-size: 34px; letter-spacing: 1px; text-transform: uppercase; flex-direction: column; gap: 14px; text-align: center; line-height: 1.1; }
  .card--front .wordmark__dot { width: 24px; height: 24px; }

  .card--back .wordmark { font-size: 22px; text-transform: uppercase; flex-direction: column; align-items: flex-start; gap: 10px; width: 196px; line-height: 1.15; }

  .divider { width: 1px; height: 150px; background: linear-gradient(to bottom, transparent, var(--steel), transparent); margin: 0 22px 0 14px; flex: none; }

  .contact__name { color: var(--brand-blue); font-weight: 700; font-size: 19px; letter-spacing: .5px; text-transform: uppercase; }
  .contact__role { color: var(--ink-light); font-weight: 600; font-size: 14px; letter-spacing: .5px; margin-bottom: 12px; }
  .contact__list { list-style: none; }
  .contact__item { display: flex; align-items: center; gap: 9px; color: var(--ink-light); font-size: 13px; font-weight: 500; line-height: 21px; }
  .contact__item svg { width: 12px; height: 12px; flex: none; fill: var(--brand-blue); }
</style>
</head>
<body>
  <section class="card card--front" aria-label="Card front">
    <div class="wordmark">
      <span class="wordmark__dot"></span>
      <span>Kestrel<br>Development</span>
    </div>
  </section>

  <section class="card card--back" aria-label="Card back">
    <div class="wordmark">
      <span class="wordmark__dot"></span>
      <span>Kestrel<br>Development</span>
    </div>
    <div class="divider"></div>
    <div class="contact">
      <p class="contact__name">Lena Hartwig</p>
      <p class="contact__role">CEO/FOUNDER</p>
      <ul class="contact__list">
        <li class="contact__item">
          <svg viewBox="0 0 12 12" aria-hidden="true"><path d="M2.5 1l2 2-1 1.5c.6 1.4 1.6 2.4 3 3L8 6.5l2 2-1.2 2.2C5 10.5 1.5 7 1.3 2.2z"/></svg>
          555 214 7730
        </li>
        <li class="contact__item">
          <svg viewBox="0 0 12 12" aria-hidden="true"><path d="M3 0h6v12H3zM4 1.5v8h4v-8zM5.5 10.3h1v.9h-1z" fill-rule="evenodd"/></svg>
          555 390 6182
        </li>
        <li class="contact__item">
          <svg viewBox="0 0 12 12" aria-hidden="true"><path d="M0 2h12v8H0zM1 3l5 3.5L11 3v-.2H1z"/></svg>
          lena@kestreldev.net
        </li>
        <li class="contact__item">
          <svg viewBox="0 0 12 12" aria-hidden="true"><circle cx="6" cy="6" r="5.5"/></svg>
          www.kestreldev.net
        </li>
      </ul>
    </div>
  </section>
</body>
</html>
```